***Flyer*** TORNILEX AUTO TRANSPORT *** Flyer***

I need a flyer design that explain my auto transport business... the design must be eye catching and draws a persons attention at first site. We Tow Cars locally in the City of Houston for a flat rate of $75... We ask that the designer make the $75 standout so it will catch the attention of the reader. Much of the content writing can be gather from my website tornilexautotransport.com - the designer can use his own images to express his design work... I will attach the logo and some samples of some reason business and post cards designs. If you chose you can also add these images in your designs if it will help.

Size of flyer is 8"x11" front and back

Automotive

Requirements
Must have
• $75 or $75.00
• (281) 555-0137
• service@tornilexautotransport.com
• www.tornilexautotransport.com
Nice to have
• WE REALLY WANT TO EARN YOUR BUSINESS
• Note: Please look at my website for content writing to create your flyer.

```html
<!DOCTYPE html>
<html lang="en">
<head>
<meta charset="utf-8">
<title>Tornilex Auto Transport Flyer</title>
<link href="https://fonts.googleapis.com/css2?family=Oswald:wght@500;700&family=Roboto:wght@400;700;900&display=swap" rel="stylesheet">
<style>
  :root {
    --red: #d0101c;
    --red-dark: #8e0710;
    --ink: #1d1d1f;
    --grey: #3c3c40;
    --paper: #ffffff;
    --night: #0c0c0d;
  }
  * { margin: 0; padding: 0; box-sizing: border-box; }
  html, body { width: 900px; height: 1200px; overflow: hidden; background: var(--night); }
  .flyer {
    position: relative; width: 900px; height: 1200px; overflow: hidden;
    background: radial-gradient(ellipse at 50% 80%, #2a2a2d 0%, var(--night) 70%);
    font-family: "Roboto", Arial, sans-serif;
  }
  .hero-photo {
    position: absolute; left: 0; top: 70px; width: 900px; height: 500px;
    background: linear-gradient(120deg, #5d6670 0%, #aab3bb 35%, #c9cfd4 55%, #7a6f72 80%, #b9b2ad 100%);
  }
  .top-frame { position: absolute; left: 0; top: 0; width: 900px; height: 260px; }
  .brand {
    position: absolute; top: 60px; left: 0; width: 900px; text-align: center;
    display: flex; justify-content: center; align-items: center; gap: 12px;
  }
  .brand-dot { width: 22px; height: 22px; border-radius: 50%; background: var(--red); }
  .brand-name {
    font-family: "Oswald", "Arial Narrow", sans-serif; font-weight: 700;
    font-size: 34px; color: var(--ink); letter-spacing: 1px;
  }
  .title-band {
    position: absolute; left: 0; top: 570px; width: 900px; height: 78px;
    background: linear-gradient(#ffffff, #d7d7d9);
    border-top: 6px solid var(--red);
  }
  .title-band h1 {
    font-family: "Oswald", "Arial Narrow", sans-serif; font-weight: 700;
    font-size: 44px; color: var(--ink); line-height: 72px; padding-left: 70px;
    letter-spacing: 1px;
  }
  .pitch {
    position: absolute; left: 0; top: 648px; width: 900px; height: 160px;
    background: var(--paper); padding: 20px 0 0 70px;
    border-bottom: 4px solid var(--red);
  }
  .pitch .lead { color: var(--red); font-size: 35px; font-weight: 700; line-height: 1.15; }
  .pitch .promise { color: var(--grey); font-size: 33px; line-height: 1.15; width: 600px; }
  .price-seal {
    position: absolute; left: 680px; top: 590px; width: 190px; height: 190px;
    border-radius: 50%; background: radial-gradient(circle at 40% 35%, #ef2a34, var(--red-dark));
    border: 8px solid var(--paper); box-shadow: 0 6px 16px rgba(0,0,0,.4);
    color: #fff; text-align: center; display: flex; flex-direction: column; justify-content: center;
  }
  .price-seal .amount { font-family: "Oswald", sans-serif; font-size: 76px; font-weight: 700; line-height: 1; }
  .price-seal .label { font-size: 18px; font-weight: 900; letter-spacing: 1px; }
  .info-panel {
    position: absolute; left: 120px; top: 840px; width: 660px; height: 320px;
    background: linear-gradient(180deg, #e0141f 0%, var(--red-dark) 100%);
    border-radius: 6px; color: #fff; text-align: center; padding: 30px 30px;
    box-shadow: 0 10px 30px rgba(0,0,0,.6);
  }
  .info-panel .about { font-size: 25px; font-weight: 700; line-height: 1.25; }
  .info-panel .about strong { font-size: 30px; }
  .info-panel .hours { margin-top: 16px; font-size: 17px; line-height: 1.3; }
  .info-panel .phone { font-family: "Oswald", sans-serif; font-size: 36px; font-weight: 700; margin-top: 6px; }
  .info-panel .small { font-size: 14px; line-height: 1.4; }
</style>
</head>
<body>
<div class="flyer">
  <div class="hero-photo" role="img" aria-label="Photo of a woman on a phone call beside a broken-down car with its hood open"></div>

  <svg class="top-frame" viewBox="0 0 900 260" aria-hidden="true">
    <polygon points="0,0 900,0 900,90 450,240 0,90" fill="#c7080f"/>
    <polygon points="0,0 900,0 900,72 450,220 0,72" fill="#ffffff"/>
    <polygon points="0,0 900,0 900,40 450,170 0,40" fill="#eeeeef"/>
    <polygon points="0,0 900,0 900,30 450,160 0,30" fill="#ffffff"/>
  </svg>
  <div class="brand">
    <span class="brand-dot"></span>
    <span class="brand-name">TORNILEX AUTO TRANSPORT</span>
  </div>

  <div class="title-band"><h1>TORNILEX AUTO TRANSPORT</h1></div>

  <div class="pitch">
    <p class="lead">We really want to earn your business!</p>
    <p class="promise">We guarantee you will only pay for towing in the city of houston</p>
  </div>

  <div class="price-seal">
    <span class="amount">$75</span>
    <span class="label">GUARANTEE</span>
  </div>

  <div class="info-panel">
    <p class="about">We are located in the city of Houston and that gives us the ability to get your vehicle towed to it's new destination <strong>in 24 hours or less</strong></p>
    <p class="hours">Contact us for any info<br>Monday - Friday: 8:00 AM - 6:00 PM</p>
    <p class="phone">(281) 555-0137</p>
    <p class="small">service@tornilexautotransport.com · www.tornilexautotransport.com</p>
    <p class="small">Closed All Major Holidays · All Cards Accepted</p>
  </div>
</div>
</body>
</html>
```